ThisIsRayWendt.com needs a modern, eye-catching business card design

My name is Ray Wendt and I own a video training (software development industry) website. I need a business card design that is eye catching for when I travel to conferences or do seminars. I would prefer something simple but bold. Something along the lines of this: https://pixvaultcdn.example/design_img/512376/40918/40918_7720341_512376_image.jpg

Note that I do not have a specific logo, but I do have an caricature I use on my site of myself. I've not attached it because I'm not really a fan of having it on my business cards. I would prefer lettering instead of an image. You can go to my website (https://thisisraywendt.example) for inspiration.

I want to add the following information on my card (the order of these, their size, and their casing is up to you):

Ray Wendt
ray@ThisIsRayWendt.example
@ThisIsRayWendt
ThisIsRayWendt.com
vidstream.example/ThisIsRayWendt

I would also like to have somewhere on the card a small ad that says "Get a free course at https://ThisIsRayWendt.example/FreeCourse". Feel free to play with that wording or layout if you need. I would prefer this text to be at the bottom of the card and subtle. Some small eye-catching thing might be ok but nothing huge or garish.

I plan on printing this card at prixa.example (https://www.prixa.example/us/design-guidelines/business-cards.html). I would like it to be the standard size (3.66" x 2.16"). I would prefer rounded corners and horizontal orientation. This is a two-side design. I would prefer the side with all of the information be primarily white but I like color text (again, flexible on that). On the front side, I like simple. Maybe just ThisIsRayWendt.com (casing on that is up to you - whatever looks and reads the best - that goes for all of the casing). As for font choices, I prefer a modern, clean font. For example, Open Sans Light can be a nice option.

Website Info (might be helpful for the card):
Color Palette

Darkest blue - #263246
Alternate blue - #2F4E6A
Light blue - #2A98C3
Orange - #FF6201
White - #FFFFFF

Font for Ray Wendt Logo

Jellyka Estryas Handwriting
http://www.typeharborfree.example/jellyka_estryas_handwriting.font

Fonts for Site Content and VidStream Thumbnails

Lovelo (bold title font)
http://www.glyphmill.example/lovelo-font/

Open Sans (body font)
http://www.letterburrow.example/fonts/open-sans

Industry/Entity Type

Software Development

Contact Information for Business Card

Ray Wendt
ray@ThisIsRayWendt.example
@ThisIsRayWendt
ThisIsRayWendt.com
vidstream.example/ThisIsRayWendt

Get a free course at https://ThisIsRayWendt.example/FreeCourse

Colors

Designer to choose colors to be used in the design.

Requirements
Nice to have
• Modern color - maybe primarily a color on the front and then that color as an accent on the back.
Should not have
• Lots of colors - I LOVE color but do not want a rainbow of colors on the card.

```html
<!DOCTYPE html>
<html lang="en">
<head>
<meta charset="utf-8">
<title>Ray Wendt — Business Card</title>
<link rel="stylesheet" href="https://fonts.googleapis.com/css2?family=Lato:ital,wght@0,400;0,700;1,700&display=swap">
<style>
  :root {
    --backdrop: #1b1b1b;
    --navy: #243246;
    --paper: #e0e0e0;
    --ink-light: #ffffff;
    --ink-soft: #e6eaf0;
    --rule: #6f7d90;
  }
  * { box-sizing: border-box; margin: 0; padding: 0; }
  html, body {
    width: 1200px;
    height: 900px;
    overflow: hidden;
    background: var(--backdrop);
    font-family: "Lato", Arial, sans-serif;
  }
  .canvas { position: relative; width: 1200px; height: 900px; }

  .card {
    position: absolute;
    top: 170px;
    width: 346px;
    height: 560px;
    box-shadow: 2px 3px 6px rgba(0,0,0,0.55);
  }
  .card--info { left: 259px; background: var(--navy); color: var(--ink-soft); }
  .card--brand { left: 631px; background: var(--paper); }

  .wordmark {
    font-family: "Lato", Arial, sans-serif;
    font-weight: 400;
    white-space: nowrap;
  }
  .card--info .wordmark {
    position: absolute;
    top: 82px;
    left: 0;
    width: 100%;
    text-align: center;
    font-size: 50px;
    color: var(--ink-light);
  }
  .card--brand .wordmark {
    position: absolute;
    left: 50%;
    top: 50%;
    font-size: 66px;
    color: var(--navy);
    transform: translate(-50%, -50%) rotate(-90deg);
  }

  .contact-list {
    position: absolute;
    top: 321px;
    left: 0;
    width: 100%;
    list-style: none;
    text-align: center;
    font-size: 16px;
    line-height: 23px;
  }
  .divider {
    position: absolute;
    top: 433px;
    left: 116px;
    width: 98px;
    height: 1px;
    background: var(--rule);
    border: 0;
  }
  .free-course {
    position: absolute;
    top: 462px;
    left: 0;
    width: 100%;
    text-align: center;
    font-size: 16px;
    line-height: 23px;
  }
  .free-course__link {
    display: block;
    font-weight: 700;
    font-style: italic;
    font-size: 15.5px;
    color: var(--ink-light);
  }
</style>
</head>
<body>
<main class="canvas">
  <section class="card card--info" aria-label="Card back with contact details">
    <h1 class="wordmark">Ray Wendt</h1>
    <ul class="contact-list">
      <li>ray@ThisIsRayWendt.example</li>
      <li>www.ThisIsRayWendt.example</li>
      <li>chirper@ThisIsRayWendt</li>
      <li>vidstream.example/ThisIsRayWendt</li>
    </ul>
    <hr class="divider">
    <p class="free-course">Get a free course at
      <span class="free-course__link">https://ThisIsRayWendt.example/FreeCourse</span>
    </p>
  </section>

  <section class="card card--brand" aria-label="Card front">
    <p class="wordmark">Ray Wendt</p>
  </section>
</main>
</body>
</html>
```